Postcard: Open Sky Circle

Text for front: HOW TO CHANGE THE WORLD IN ONE [note: the word "one" should be underlined] STEPHint: It's up to you...[Note: add arrow or something to indicate "turn over"]Text for back: You're going to spend your entire life with someone you can never get away from. (Guess who?) Wouldn't you rather that person #OpenSkyCircle than judgmental or critical? BE the change you want to see! Visit www.OpenSkyCircle-hub.example for daily Dawn Pebbles and community. PLEASE JOIN US![Note: add logo to left half of back side]Font preference for text: Josefin sans

Target Market(s)

People who would be attracted to Corvane church - teravian perennist message. It's spiritual without being overtly religious, so the target market is probably early 30s and up but ideally won't turn off Millennials (folks under 30). It should attract attention of people who are open-minded and committed to progressive social change, tired of an atmosphere of hate-mongering and divisiveness.

Requirements
Nice to have
• It would be nice to convey a sense of challenge - there is an idea of "dawn pebbles" so something related to fire/sparks is appropriate. This is meant to evoke a deeper, divine love more than a sense of romantic love. This love is more fierce than fluffy! Yet it calls us to be our best selves.
Should not have
• Please avoid excessive pink - just the logo is enough, as this design needs to appeal to men as well as women.

```html
<!DOCTYPE html>
<html lang="en">
<head>
<meta charset="utf-8">
<title>Open Sky Circle Postcard</title>
<link href="https://fonts.googleapis.com/css2?family=Josefin+Sans:wght@300;400;700&display=swap" rel="stylesheet">
<style>
  :root {
    --page-bg: #d9d9d9;
    --card-bg: #ffffff;
    --accent: #e8407a;
    --accent-soft: #f08aab;
    --ink-grey: #7a7a7a;
    --ink-dark: #3a3a3a;
    --band-grey: #c4c4c4;
    --ribbon: #3b3b3b;
  }
  * { margin: 0; padding: 0; box-sizing: border-box; }
  html, body { width: 1200px; height: 1200px; overflow: hidden; }
  body {
    background: var(--page-bg);
    font-family: "Josefin Sans", sans-serif;
    position: relative;
  }
  .postcard {
    position: absolute;
    left: 127px;
    width: 946px;
    height: 540px;
    background: var(--card-bg);
    overflow: hidden;
    box-shadow: 0 4px 14px rgba(0,0,0,0.15);
  }
  .postcard--front { top: 40px; }
  .postcard--back { top: 620px; }

  /* Front */
  .headline {
    position: absolute;
    left: 190px;
    top: 48px;
    line-height: 1;
  }
  .headline__line { display: block; white-space: nowrap; }
  .headline__how { font-weight: 300; font-size: 68px; color: var(--accent); letter-spacing: 2px; }
  .headline__world { font-weight: 700; font-size: 96px; color: var(--accent); margin-top: 2px; }
  .headline__step { font-weight: 300; font-size: 96px; color: var(--ink-grey); margin-top: 4px; }
  .headline__one {
    text-decoration: underline;
    text-decoration-color: var(--accent);
    text-decoration-thickness: 4px;
    text-underline-offset: 14px;
  }
  .turn-ribbon { position: absolute; left: 0; top: 330px; }
  .hint {
    position: absolute;
    left: 40px;
    top: 344px;
    font-size: 30px;
    color: #ffffff;
    font-weight: 400;
  }
  .hint__label { color: var(--accent); font-weight: 700; }

  /* Back */
  .brand {
    position: absolute;
    left: 50px;
    top: 90px;
    display: flex;
    align-items: center;
    gap: 18px;
  }
  .brand__mark {
    width: 150px;
    height: 150px;
    border-radius: 50%;
    background: radial-gradient(circle at 40% 40%, var(--accent-soft), var(--accent));
  }
  .brand__name {
    font-size: 34px;
    font-weight: 400;
    color: var(--accent);
    line-height: 1.15;
    width: 160px;
  }
  .message {
    position: absolute;
    left: 470px;
    top: 150px;
    width: 440px;
    color: var(--ink-dark);
  }
  .message__body { font-size: 15px; line-height: 1.35; font-weight: 400; }
  .message__visit { font-size: 22px; margin-top: 18px; }
  .message__url { color: var(--accent); font-weight: 700; font-size: 22px; word-break: break-all; }
  .message__daily { font-size: 21px; margin-top: 8px; }
  .join-band {
    position: absolute;
    left: 0;
    top: 410px;
    width: 890px;
    height: 86px;
    background: var(--band-grey);
    color: #ffffff;
    font-size: 74px;
    font-weight: 400;
    line-height: 96px;
    padding-left: 30px;
    white-space: nowrap;
    letter-spacing: 1px;
  }
</style>
</head>
<body>

<section class="postcard postcard--front">
  <h1 class="headline">
    <span class="headline__line headline__how">HOW TO CHANGE</span>
    <span class="headline__line headline__world">THE WORLD</span>
    <span class="headline__line headline__step">IN <span class="headline__one">ONE</span> STEP</span>
  </h1>
  <svg class="turn-ribbon" width="946" height="140" viewBox="0 0 946 140" aria-hidden="true">
    <path d="M0 0 H580 C640 0 650 70 700 70 H860 V56 L900 80 L860 104 V90 H700 C630 90 630 40 560 40 H0 Z" fill="var(--ribbon)"/>
  </svg>
  <p class="hint"><span class="hint__label">Hint:</span> It's up to you...</p>
</section>

<section class="postcard postcard--back">
  <div class="brand">
    <div class="brand__mark"></div>
    <div class="brand__name">Open Sky Circle</div>
  </div>
  <div class="message">
    <p class="message__body">You're going to spend your entire life with someone you can never get away from. (Guess who?) Wouldn't you rather that person #OpenSkyCircle than judgmental or critical? BE the change you want to see!</p>
    <p class="message__visit">Visit <span class="message__url">www.OpenSkyCircle-hub.example</span></p>
    <p class="message__daily">for daily Dawn Pebbles and community</p>
  </div>
  <div class="join-band">PLEASE JOIN US!</div>
</section>

</body>
</html>
```